Professional banners for an eyewear company

I have 3 images which need to be made into banners. Size 990 x 370, with a 10 pixel white border at top and bottom of banner.

They all need to be adjusted to make the colours better and less bright.
All will need some writing written on them with a nice serif font.

Banner 1 text: Handcrafted luxury eyewear, with a purpose...
Banner 2 text: Half of our profits go to help malnourished children in India
Banner 3 text: 10% of your first order, use code: First Order

On our homepage these 3 banners will alternate, so they need to look good together.

Tips
Please take a look at the banners on the lunvoreck.com homepage, this is kind of how I want the text to be displayed, and they use good colours.

The backgrounds on Banners 2 & 3 can be changed.
Banner 3 background if you can change to a nice colour, as per lunvoreck.com homepage.
Updates

Hi, just a quick update, thank you for all the designs submitted so far, please keep in mind that the brand is a luxury high-end brand so designs will need to reflect this.

Industry/Entity Type

Eyewear

```html
<!DOCTYPE html>
<html lang="en">
<head>
<meta charset="utf-8">
<title>Eyewear Homepage Banners</title>
<link rel="stylesheet" href="https://fonts.googleapis.com/css2?family=Cinzel:wght@400;600&family=Federo&display=swap">
<style>
  :root {
    --paper: #ffffff;
    --frame: #1a1a1a;
    --plum: #806d82;
    --plum-glow: #c9bccb;
    --plum-text: #d9cfd9;
    --sage: #b0b5b2;
    --sage-glow: #e6e8e6;
    --ink: #3f3f3f;
    --sand-band: linear-gradient(90deg, #b8aa9e 0%, #cdc0b4 40%, #cdc0b4 60%, #b8aa9e 100%);
    --plum-band: linear-gradient(90deg, #6e5b70 0%, #a595a6 50%, #6e5b70 100%);
    --navy: #3c4155;
    --navy-band: linear-gradient(90deg, #4a5068 0%, #5a6078 50%, #4a5068 100%);
    --navy-glow: #8d92a3;
    --rose: #d4a6a8;
    --pale: #c7c9d2;
  }
  * { margin: 0; padding: 0; box-sizing: border-box; }
  html, body { width: 1071px; height: 1200px; overflow: hidden; background: var(--paper); }
  .canvas {
    position: relative; width: 1071px; height: 1200px;
    background: var(--paper); border: 1px solid var(--frame); overflow: hidden;
  }
  .banner { position: absolute; left: 1px; width: 1068px; }
  .banner--purpose { top: 11px; height: 380px; background: var(--plum); }
  .banner--offer { top: 410px; height: 379px; background: var(--sage); }
  .banner--giving { top: 810px; height: 378px; background: var(--navy); }

  .notch {
    position: absolute; left: 486px; width: 98px; height: 44px;
    background: var(--paper); border-radius: 50%; z-index: 5;
  }

  .photo { position: absolute; }
  .photo--glasses {
    left: 96px; top: 120px; width: 364px; height: 230px;
    background: radial-gradient(ellipse at 55% 45%, var(--plum-glow) 0%, #9c8b9e 35%, var(--plum) 70%);
  }
  .photo--model {
    left: 663px; top: 38px; width: 337px; height: 341px;
    background: radial-gradient(ellipse at 30% 55%, var(--sage-glow) 0%, #c9b3a2 35%, #a88068 55%, var(--sage) 85%);
  }
  .photo--child {
    left: 132px; top: 52px; width: 285px; height: 326px;
    background: radial-gradient(ellipse at 50% 45%, var(--navy-glow) 0%, #8a6f5a 35%, #7fa63a 70%, var(--navy) 95%);
  }

  .copy { position: absolute; text-align: center; }
  .serif-caps { font-family: "Cinzel", serif; }
  .display { font-family: "Federo", serif; }

  .band {
    position: absolute; display: flex; align-items: center; justify-content: center;
    color: var(--paper);
  }

  /* Banner 1 */
  .purpose__lead { left: 581px; top: 118px; width: 401px; font-size: 25px; letter-spacing: 2px; color: var(--plum-text); font-variant: small-caps; }
  .purpose__title { left: 560px; top: 163px; width: 440px; font-size: 32px; letter-spacing: 3px; color: var(--paper); }
  .purpose__with { left: 581px; top: 231px; width: 401px; font-size: 15px; color: var(--plum-text); font-variant: small-caps; letter-spacing: 1px; }
  .band--purpose { left: 580px; top: 253px; width: 402px; height: 51px; background: var(--plum-band); font-size: 23px; }

  /* Banner 2 */
  .offer__line { position: absolute; left: 91px; top: 146px; display: flex; align-items: baseline; gap: 14px; color: var(--ink); white-space: nowrap; }
  .offer__pct { font-size: 44px; }
  .offer__small { font-size: 15px; }
  .offer__big { font-size: 29px; margin-left: 10px; }
  .offer__code-label { left: 102px; top: 232px; width: 402px; font-size: 12px; color: var(--ink); }
  .band--offer { left: 102px; top: 256px; width: 402px; height: 50px; background: var(--sand-band); font-size: 24px; }

  /* Banner 3 */
  .giving__line1 { left: 560px; top: 108px; width: 430px; color: var(--paper); white-space: nowrap; display: flex; align-items: baseline; justify-content: center; gap: 14px; }
  .giving__half { font-size: 26px; color: var(--pale); }
  .giving__half b { font-weight: 400; font-size: 48px; }
  .giving__tiny { font-size: 15px; letter-spacing: 1px; color: var(--pale); }
  .giving__profits { font-size: 23px; }
  .giving__goto { left: 572px; top: 163px; width: 403px; font-size: 11px; letter-spacing: 3px; color: var(--pale); }
  .band--giving { left: 572px; top: 192px; width: 403px; height: 44px; background: var(--navy-band); color: var(--rose); font-size: 38px; letter-spacing: 10px; }
  .giving__malnourished { left: 560px; top: 251px; width: 430px; font-size: 17px; letter-spacing: 9px; color: var(--pale); }
  .giving__line5 { left: 560px; top: 290px; width: 430px; display: flex; align-items: baseline; justify-content: center; gap: 14px; color: var(--paper); }
  .giving__children { font-size: 36px; }
  .giving__india { font-size: 22px; color: var(--pale); }
</style>
</head>
<body>
<main class="canvas">

  <section class="banner banner--purpose">
    <div class="photo photo--glasses" role="img" aria-label="Photo of black handcrafted eyeglasses with a soft reflection"></div>
    <p class="copy serif-caps purpose__lead">Handcrafted</p>
    <h1 class="copy serif-caps purpose__title" style="font-weight:400">LUXURY EYEWEAR,</h1>
    <p class="copy serif-caps purpose__with">With</p>
    <div class="band band--purpose serif-caps">A PURPOSE...</div>
  </section>

  <section class="banner banner--offer">
    <div class="photo photo--model" role="img" aria-label="Photo of a red-haired woman in sunglasses and a polka-dot blouse looking surprised"></div>
    <div class="offer__line display">
      <span class="offer__pct">10%</span>
      <span class="offer__small">OF YOUR</span>
      <span class="offer__big">FIRST ORDER,</span>
    </div>
    <p class="copy display offer__code-label">USE CODE:</p>
    <div class="band band--offer display">FIRST ORDER</div>
  </section>

  <section class="banner banner--giving">
    <div class="photo photo--child" role="img" aria-label="Photo of a smiling young girl in a green top"></div>
    <div class="copy giving__line1 serif-caps">
      <span class="giving__half"><b>H</b>ALF</span>
      <span class="giving__tiny">OF</span>
      <span class="giving__tiny">OUR</span>
      <span class="giving__profits">PROFITS</span>
    </div>
    <p class="copy serif-caps giving__goto">GO TO</p>
    <div class="band band--giving serif-caps">HELP</div>
    <p class="copy serif-caps giving__malnourished">MALNOURISHED</p>
    <div class="copy giving__line5 display">
      <span class="giving__children">CHILDREN</span>
      <span class="giving__tiny">IN</span>
      <span class="giving__india">INDIA</span>
    </div>
  </section>

  <div class="notch" style="top:-22px"></div>
  <div class="notch" style="top:378px"></div>
  <div class="notch" style="top:777px"></div>
  <div class="notch" style="top:1176px"></div>

</main>
</body>
</html>
```